Bellmont Planners, LLC Stationary

Bellmont Planners, LLC is a new financial planning and consulting company. We are looking for designs on business cards, letterhead, envelopes, and anything else that would be useful. Our preference for business card design is two sided. We are looking for a professional and clean look with incorporating the logo and patriotic feel. Thank you to all who participate and good luck!

```html
<!DOCTYPE html>
<html lang="en">
<head>
<meta charset="utf-8">
<title>Bellmont Planners, LLC — Stationery</title>
<link href="https://fonts.googleapis.com/css2?family=Fira+Sans:wght@400;500;600&display=swap" rel="stylesheet">
<style>
  :root {
    --navy: #143f6b;
    --red: #e30613;
    --paper: #ffffff;
    --ink: #2b2b2b;
    --backdrop-light: #f2f2f2;
    --backdrop-dark: #bdbdbd;
  }
  * { box-sizing: border-box; margin: 0; padding: 0; }
  html, body { width: 1200px; height: 1200px; overflow: hidden; }
  body {
    position: relative;
    font-family: "Fira Sans", Arial, sans-serif;
    background: radial-gradient(circle at 40% 35%, var(--backdrop-light), var(--backdrop-dark));
  }
  .sheet {
    position: absolute;
    background: var(--paper);
    box-shadow: 0 6px 22px rgba(0,0,0,.18);
    overflow: hidden;
  }
  .brand {
    display: flex;
    align-items: center;
    gap: 10px;
    color: var(--navy);
    font-weight: 600;
    letter-spacing: .5px;
    white-space: nowrap;
  }
  .brand-mark { background: var(--red); flex: none; }
  .band {
    position: absolute;
    left: 0; right: 0; bottom: 0;
    background: var(--navy);
    color: #fff;
  }

  /* Letterhead */
  .letterhead { left: 640px; top: 90px; width: 500px; height: 707px; }
  .letterhead .brand { position: absolute; top: 44px; right: 40px; font-size: 22px; }
  .letterhead .brand-mark { width: 16px; height: 16px; }
  .letterhead .band { height: 78px; padding: 16px 32px 0 40px; font-size: 13px; line-height: 1.7; letter-spacing: .3px; }

  /* Envelope */
  .envelope { left: 60px; top: 700px; width: 540px; height: 280px; }
  .envelope .brand { position: absolute; top: 36px; left: 34px; font-size: 22px; }
  .envelope .brand-mark { width: 16px; height: 16px; }
  .envelope .band { height: 52px; padding: 17px 0 0 40px; font-size: 13px; letter-spacing: .3px; }

  /* Business cards */
  .card { width: 300px; height: 170px; }
  .card-front { left: 80px; top: 120px; }
  .card-back { left: 80px; top: 330px; display: flex; align-items: center; justify-content: center; }
  .card-back .brand { font-size: 18px; gap: 8px; }
  .card-back .brand-mark { width: 12px; height: 12px; }

  .contact { position: absolute; top: 16px; right: 18px; text-align: right; }
  .contact-name { color: var(--red); font-weight: 600; font-size: 14px; letter-spacing: 1.2px; text-transform: uppercase; }
  .contact-role { color: var(--ink); font-size: 8px; margin-bottom: 8px; }
  .contact-line { display: flex; justify-content: flex-end; align-items: center; gap: 5px; color: var(--ink); font-size: 8px; line-height: 1.65; }
  .contact-line svg { width: 8px; height: 8px; fill: var(--red); flex: none; }
  .card-front .band { height: 40px; padding: 8px 18px 0 0; text-align: right; font-size: 8px; line-height: 1.5; }
</style>
</head>
<body>

  <section class="sheet letterhead" aria-label="Letterhead">
    <div class="brand"><span class="brand-mark"></span>Bellmont Planners, LLC</div>
    <footer class="band">
      <p>Dummy City, Dummy Country, Dummy State</p>
      <p>+01 55501 2040 | www.bellmontplanners.com | info@bellmontplanners.com</p>
    </footer>
  </section>

  <section class="sheet envelope" aria-label="Envelope">
    <div class="brand"><span class="brand-mark"></span>Bellmont Planners, LLC</div>
    <footer class="band">
      <p>Dummy City, Dummy Country, Dummy State</p>
    </footer>
  </section>

  <section class="sheet card card-front" aria-label="Business card, front">
    <div class="contact">
      <p class="contact-name">Nora Whitfield</p>
      <p class="contact-role">Director</p>
      <p class="contact-line">+01 55502 7314
        <svg viewBox="0 0 10 10"><rect x="2.5" y="0.5" width="5" height="9" rx="1"/></svg></p>
      <p class="contact-line">+01 55501 2040
        <svg viewBox="0 0 10 10"><path d="M2 1l2 2-1 1.5c.8 1.3 1.7 2.2 3 3L7.5 6l2 2-1.5 1.5C4.5 9 1 5.5.5 2z"/></svg></p>
      <p class="contact-line">www.bellmontplanners.com
        <svg viewBox="0 0 10 10"><circle cx="5" cy="5" r="4.5"/></svg></p>
      <p class="contact-line">nora@bellmontplanners.com
        <svg viewBox="0 0 10 10"><path d="M0 2h10v6H0z M0 2l5 3.5L10 2" /></svg></p>
    </div>
    <footer class="band">
      <p>Dummy City</p>
      <p>Dummy Country, Dummy State</p>
    </footer>
  </section>

  <section class="sheet card card-back" aria-label="Business card, back">
    <div class="brand"><span class="brand-mark"></span>Bellmont Planners, LLC</div>
  </section>

</body>
</html>
```